copper kettle drywall repair web page

need a web presence for my company. we are a golf themed drywall repair company. need a home page, contact us, photos, about us, services possible payment option

```html
<!DOCTYPE html>
<html lang="en">
<head>
<meta charset="utf-8">
<title>Copper Kettle Drywall Repair</title>
<link href="https://fonts.googleapis.com/css2?family=Montserrat:wght@400;500;600&family=Roboto:wght@400;500&display=swap" rel="stylesheet">
<style>
  :root {
    --gold: #f2c12e;
    --gold-dark: #e0a814;
    --navy: #262d6b;
    --nav-top: #4a6ad0;
    --nav-bottom: #1d2d80;
    --text: #7a7a7a;
    --heading: #4a4a4a;
    --white: #ffffff;
  }
  * { margin: 0; padding: 0; box-sizing: border-box; }
  html, body { width: 997px; height: 1200px; overflow: hidden; background: var(--white); }
  body { position: relative; font-family: "Roboto", sans-serif; color: var(--text); }

  .top-rule, .bottom-rule { position: absolute; left: 0; width: 997px; height: 2px; background: var(--gold); }
  .top-rule { top: 0; }
  .bottom-rule { top: 1197px; height: 3px; }

  .brand { position: absolute; left: 93px; top: 44px; display: flex; align-items: center; gap: 10px; }
  .brand-mark { width: 30px; height: 30px; border-radius: 50%; background: var(--navy); }
  .brand-name { font-family: "Montserrat", sans-serif; font-weight: 600; font-size: 15px; color: var(--navy); line-height: 1.2; }

  .contact { position: absolute; right: 93px; top: 48px; text-align: right; font-size: 12px; color: #222; }
  .contact-line { display: flex; justify-content: flex-end; align-items: center; gap: 7px; height: 16px; margin-bottom: 10px; }
  .contact-line svg { width: 13px; height: 12px; }

  .main-nav { position: absolute; left: 82px; top: 120px; width: 833px; height: 43px; border-radius: 3px;
    background: linear-gradient(var(--nav-top), var(--nav-bottom)); }
  .main-nav a { position: absolute; top: 17px; font-family: "Montserrat", sans-serif; font-size: 10.5px; font-weight: 500;
    color: var(--white); text-decoration: none; }
  .main-nav a.active { color: var(--gold); }
  .social { position: absolute; right: 13px; top: 12px; display: flex; gap: 5px; }
  .social span { width: 19px; height: 19px; border-radius: 50%; border: 1.5px solid var(--white); background: rgba(255,255,255,0.15); }

  .scenery { position: absolute; left: 0; top: 170px; width: 997px; height: 966px;
    background: linear-gradient(180deg, #c9741a 0%, #e8a23a 14%, #6b4a1a 34%, #2f4a12 52%, #4f8a1e 70%, #2c5a12 100%); }

  .panel { position: absolute; left: 82px; top: 180px; width: 833px; height: 932px; background: var(--white); }

  .hero { position: absolute; left: 11px; top: 14px; width: 803px; height: 412px;
    background: linear-gradient(100deg, #b85a5a 0%, #c98a86 22%, #7faa98 40%, #8fb9a8 60%, #d9dcd8 78%, #a9b7ae 100%); }
  .hero-title { position: absolute; left: 385px; top: 238px; font-family: "Montserrat", sans-serif; font-weight: 500;
    font-size: 43px; color: var(--navy); letter-spacing: 0.5px; }
  .hero-dots { position: absolute; left: 357px; top: 389px; display: flex; align-items: center; gap: 4px; }
  .hero-dots span { width: 9px; height: 9px; border-radius: 50%; border: 1.5px solid var(--white); }
  .hero-dots span.on { background: var(--gold); border-color: var(--gold); }

  .section-title { position: absolute; left: 0; width: 833px; text-align: center; font-family: "Montserrat", sans-serif;
    font-weight: 500; font-size: 17px; color: var(--navy); }
  .intro { position: absolute; left: 45px; top: 486px; width: 743px; text-align: center; font-size: 9.5px; line-height: 21.5px; }

  .divider { position: absolute; left: 354px; width: 126px; height: 8px; }

  .feature { position: absolute; top: 595px; width: 398px; }
  .feature-icon { position: absolute; left: 0; top: 0; width: 98px; height: 82px;
    background: linear-gradient(var(--gold), var(--gold-dark)); display: flex; align-items: center; justify-content: center; }
  .feature-title { position: absolute; left: 114px; top: -1px; width: 285px; font-family: "Montserrat", sans-serif;
    font-size: 12.5px; line-height: 17.5px; color: var(--heading); }
  .feature-text { position: absolute; left: 114px; top: 38px; width: 285px; font-size: 9px; line-height: 17px; }

  .gallery { position: absolute; left: 11px; top: 775px; display: flex; gap: 22px; }
  .gallery-item { width: 187px; height: 119px; border: 2px solid var(--gold); box-shadow: 0 4px 4px rgba(0,0,0,0.3); }

  .site-footer { position: absolute; left: 0; top: 1136px; width: 997px; height: 61px; font-size: 10px; color: #333; }
  .site-footer .links { position: absolute; left: 92px; top: 28px; }
  .site-footer .copyright { position: absolute; right: 92px; top: 28px; }
</style>
</head>
<body>
  <div class="top-rule"></div>

  <header>
    <div class="brand">
      <span class="brand-mark"></span>
      <span class="brand-name">Copper Kettle<br>Drywall Repair</span>
    </div>
    <div class="contact">
      <div class="contact-line">
        <svg viewBox="0 0 13 12"><rect x="0" y="1" width="13" height="10" rx="1" fill="#f2c12e"/><path d="M0 2 L6.5 7 L13 2" stroke="#fff" stroke-width="1.2" fill="none"/></svg>
        hello@copperkettledrywall.com
      </div>
      <div class="contact-line">
        <svg viewBox="0 0 13 12"><rect x="0.5" y="0" width="12" height="12" rx="2" fill="#f2c12e"/><path d="M4 3 L5.5 5 L4.8 6 Q5.8 7.8 7.2 8.3 L8.2 7.5 L10 9 L9 10 Q5 9.5 3 4 Z" fill="#fff"/></svg>
        555 014 2700
      </div>
    </div>
    <nav class="main-nav">
      <a class="active" href="#" style="left:30px">HOME</a>
      <a href="#" style="left:131px">ABOUT US</a>
      <a href="#" style="left:253px">PHOTOS</a>
      <a href="#" style="left:365px">SERVICES</a>
      <a href="#" style="left:484px">CONTACT US</a>
      <div class="social"><span></span><span></span><span></span><span></span></div>
    </nav>
  </header>

  <div class="scenery" role="img" aria-label="Golf course fairway at sunset with trees against an orange sky"></div>

  <main class="panel">
    <div class="hero" role="img" aria-label="Worker in a checked shirt sanding a patched drywall with a hand sander">
      <div class="hero-title">DRYWALL REPAIR</div>
      <div class="hero-dots">
        <svg width="8" height="9" viewBox="0 0 8 9"><path d="M2 1 L6 4.5 L2 8" stroke="#fff" stroke-width="1.3" fill="none"/></svg>
        <span></span><span></span><span class="on"></span><span></span><span></span><span></span>
        <svg width="8" height="9" viewBox="0 0 8 9"><rect x="1.5" y="1" width="1.4" height="7" fill="#fff"/><rect x="5" y="1" width="1.4" height="7" fill="#fff"/></svg>
      </div>
    </div>

    <h1 class="section-title" style="top:457px">WELCOME TO COPPER KETTLE DRYWALL REPAIR</h1>
    <p class="intro">Ut wisi enim ad minim veniam, quis nostrud exerci tation ullamcorper suscipit lobortis nisl ut aliquip ex ea commodo consequat. Duis autem vel eum iriure dolor in hendrerit in vulputate velit esse molestie consequat, vel illum dolore eu feugiat nulla facilisis at vero eros et accumsan et iusto odio dignissim qui blandit praesent luptatum zzril delenit augue duis dolore te feugait nulla facilisi.</p>

    <svg class="divider" style="top:558px" viewBox="0 0 126 8">
      <line x1="0" y1="4" x2="126" y2="4" stroke="#f3ead0" stroke-width="1"/>
      <path d="M50 1 L53 4 L50 7 L47 4Z M63 1 L66 4 L63 7 L60 4Z M76 1 L79 4 L76 7 L73 4Z" fill="#e0a814"/>
    </svg>

    <section class="feature" style="left:11px">
      <div class="feature-icon">
        <svg width="46" height="46" viewBox="0 0 46 46"><path d="M40 4 Q43 6 40 10 L26 26 L21 21 L36 6 Q38 3 40 4Z" fill="#262d6b"/><path d="M19 23 L24 28 Q22 38 10 40 Q5 40 4 37 Q10 36 11 30 Q12 24 19 23Z" fill="#262d6b"/></svg>
      </div>
      <h2 class="feature-title">LOREM IPSUM DOLOR SIT AMET, CONSE CTETUER ADIPSCING ELIT, SED DIAM</h2>
      <p class="feature-text">Duis autem vel eum iriure dolor in hendrerit in vulputate velit esse molestie consequat, vel illum dolore eu feugiat nulla facilisis at vero eros et accumsan et iusto odio dignissim qui blandit.</p>
    </section>

    <section class="feature" style="left:427px">
      <div class="feature-icon">
        <svg width="44" height="44" viewBox="0 0 44 44"><rect x="3" y="20" width="9" height="18" rx="1" fill="#262d6b"/><path d="M14 20 L22 8 Q25 4 27 8 L25 17 L37 17 Q41 18 40 22 L37 36 Q36 39 32 39 L14 39Z" fill="#262d6b"/></svg>
      </div>
      <h2 class="feature-title">UT WISI ENIM AD MINIM VENIAM, QUIS NOSTRUD EXERCI TATION ULLA</h2>
      <p class="feature-text">Duis autem vel eum iriure dolor in hendrerit in vulputate velit esse molestie consequat, vel illum dolore eu feugiat nulla facilisis at vero eros et accumsan et iusto odio dignissim qui blandit.</p>
    </section>

    <svg class="divider" style="top:707px" viewBox="0 0 126 8">
      <line x1="0" y1="4" x2="126" y2="4" stroke="#f3ead0" stroke-width="1"/>
      <path d="M50 1 L53 4 L50 7 L47 4Z M63 1 L66 4 L63 7 L60 4Z M76 1 L79 4 L76 7 L73 4Z" fill="#e0a814"/>
    </svg>

    <h2 class="section-title" style="top:733px">OUR GALERY</h2>
    <div class="gallery">
      <div class="gallery-item" role="img" aria-label="Worker fitting a ceiling drywall panel" style="background:linear-gradient(135deg,#e8e6e2,#b9c4d2 60%,#6f8fb8)"></div>
      <div class="gallery-item" role="img" aria-label="Worker sanding a green drywall patch" style="background:linear-gradient(135deg,#c98a86,#8fb9a8 50%,#dcdcd8)"></div>
      <div class="gallery-item" role="img" aria-label="Worker applying plaster with a trowel" style="background:linear-gradient(135deg,#d9d9d6,#9aa0a6 50%,#4d7fc0)"></div>
      <div class="gallery-item" role="img" aria-label="Worker in a hard hat screwing drywall to a ceiling" style="background:linear-gradient(135deg,#b8b8b6,#8a8c8e 50%,#3a3a3c)"></div>
    </div>
  </main>

  <footer class="site-footer">
    <div class="links">Privacy Policy | Sitemap</div>
    <div class="copyright">Copyright © 2015 Copper Kettle Drywall repair. All Right Reserved.</div>
  </footer>
  <div class="bottom-rule"></div>
</body>
</html>
```